Event Poster - Tarona Mist Fest 2018 (Need ASAP)

Create a poster for an upcoming vape event, located in Waikato, Hamilton, New Zealand.

Mist Fest is an event where lots of shops come to a location, and the public are welcomed and they all vape, buy vape products, socialize, drink beer and have fun.

VISIT THE EVENT WEBSITE FOR INFO - www.taronamistfest.co.nz

We have created a website at, as you can see the logo and design is a bit boring and plain, so we dont really want it to look anything like that, The logo that is created to suit the poster will be able to be

Need a poster done up so we can send it around, post it up on boards, share on social media etc

I have attached previous events from nearby towns, for reference, but I want something much better.

Target Market(s)

25-45 Male / Female

Requirements
Must have
• - Tarona Mist Fest 2018
• - Saturday, 2nd June 2018
• - 12-10pm
• - R18 Event (important for public to know)
• - Vendors, Prizes, Comps, E Juice Awards, Entertainment, Giveaways & More
• - The Corner Alehouse (52 Mulgrave Rd, Kerepuni, Hamilton)
• - mention something along lines "Come To Tarona's First Mist Fest"
• - "Get Your Tickets from www.taronamistfest.co.nz TODAY"
• - I want people to know they can buy it from a store as well "The Cloud Barn"
Nice to have
• Our City colors are Red,Yellow,Black which is symbolic for "Waikato" so it would be nice to have those integrated in there. Alot of the other Mist Fest events have dark, bogan, amateur look done to them, so I want ours to be just a much better version.
• To Clarify, Hamilton is a city inside the Waikato
• I might want to put sponsors on there as well, possibly 10-20, but maybe only a few if space is a problem

```html
<!DOCTYPE html>
<html lang="en">
<head>
<meta charset="utf-8">
<title>Tarona Mist Fest 2018</title>
<link rel="stylesheet" href="https://fonts.googleapis.com/css2?family=Anton&family=Lobster&family=Roboto:wght@900&display=swap">
<style>
  :root {
    --yellow: #fff27a;
    --yellow-bright: #fff45c;
    --paper: #fffbe2;
    --red: #e8231c;
    --black: #141414;
    --white: #ffffff;
  }
  * { margin: 0; padding: 0; box-sizing: border-box; }
  html, body { width: 849px; height: 1200px; overflow: hidden; background: var(--yellow); }
  .poster {
    position: relative;
    width: 849px;
    height: 1200px;
    overflow: hidden;
    background: var(--yellow);
    font-family: "Anton", "Impact", sans-serif;
    color: var(--black);
  }
  .title-block { position: absolute; left: 0; top: 0; }
  .title-city { font-family: "Anton", sans-serif; fill: var(--yellow-bright); }
  .title-city-shadow { font-family: "Anton", sans-serif; fill: var(--red); }
  .title-main { font-family: "Anton", sans-serif; fill: var(--red); stroke: var(--yellow-bright); stroke-width: 2; }
  .title-main-shadow { font-family: "Anton", sans-serif; fill: var(--black); }
  .title-year { font-family: "Anton", sans-serif; fill: var(--black); }
  .title-year-shadow { font-family: "Anton", sans-serif; fill: var(--yellow-bright); }

  .event-date {
    position: absolute; left: 0; top: 488px; width: 849px;
    text-align: center;
    font-size: 56px; line-height: 1;
    letter-spacing: 0.5px;
    color: var(--black);
    text-shadow: 4px 3px 0 var(--red);
    white-space: nowrap;
  }

  .venue { position: absolute; left: 0; top: 565px; width: 849px; height: 147px; }
  .venue-shape { position: absolute; left: 0; top: 0; }
  .venue-name {
    position: absolute; left: 0; top: 10px; width: 849px;
    text-align: center;
    font-family: "Lobster", cursive;
    font-weight: 400;
    font-size: 68px; line-height: 1.15;
    color: var(--yellow-bright);
    text-shadow: 4px 4px 0 var(--red);
    white-space: nowrap;
  }
  .venue-address {
    position: absolute; left: 0; top: 104px; width: 849px;
    text-align: center;
    font-size: 27px; line-height: 1;
    color: var(--yellow-bright);
    white-space: nowrap;
  }

  .features {
    position: absolute; left: 0; top: 738px; width: 849px;
    text-align: center;
    font-size: 38px; line-height: 56px;
    color: var(--black);
    white-space: nowrap;
  }

  .tickets-heading {
    position: absolute; left: 0; top: 852px; width: 849px;
    text-align: center;
    font-family: "Lobster", cursive;
    font-weight: 400;
    font-size: 48px; line-height: 1.1;
    color: var(--red);
    text-shadow: 3px 3px 0 var(--black);
    white-space: nowrap;
  }
  .age-badge {
    position: absolute; top: 900px;
    width: 82px; height: 82px; border-radius: 50%;
    background: var(--black);
    display: flex; align-items: center; justify-content: center;
    font-size: 32px;
    color: var(--yellow-bright);
    text-shadow: 2px 2px 0 var(--red);
  }
  .age-badge--left { left: 68px; }
  .age-badge--right { left: 699px; }
  .tickets-url {
    position: absolute; left: 0; top: 924px; width: 849px;
    text-align: center;
    font-family: "Roboto", Arial, sans-serif; font-weight: 900;
    font-size: 27px; line-height: 1;
    color: var(--black);
  }
  .tickets-store {
    position: absolute; left: 330px; top: 960px;
    font-size: 27px; line-height: 1;
    color: var(--black);
    white-space: nowrap;
  }

  .closing-banner { position: absolute; left: 0; top: 1002px; width: 849px; height: 76px; }
  .closing-shape { position: absolute; left: 0; top: 0; }
  .closing-text {
    position: absolute; left: 0; top: 11px; width: 849px;
    text-align: center;
    font-family: "Lobster", cursive;
    font-weight: 400;
    font-size: 44px; line-height: 1.15;
    color: var(--yellow-bright);
    text-shadow: 3px 3px 0 var(--black);
    white-space: nowrap;
  }

  .sponsors {
    position: absolute; left: 113px; top: 1096px;
    display: flex; gap: 6px; height: 52px;
  }
  .sponsor {
    display: flex; align-items: center; justify-content: center;
    height: 52px; padding: 0 5px;
    font-size: 12px; line-height: 1.1; text-align: center;
  }
  .sponsor--dark { background: var(--black); color: var(--white); }
  .sponsor--light { background: var(--white); color: var(--black); border: 1px solid #cfcfcf; }
</style>
</head>
<body>
<main class="poster">

  <svg class="title-block" width="849" height="470" viewBox="0 0 849 470">
    <polygon points="60,50 780,50 780,60 60,150" fill="var(--black)"/>
    <polygon points="60,150 780,60 780,318 60,458" fill="var(--paper)"/>
    <polygon points="780,318 780,458 60,458" fill="var(--red)"/>
    <g transform="rotate(-7.5 420 250)">
      <text class="title-city-shadow" x="77" y="131" font-size="62" textLength="255" lengthAdjust="spacingAndGlyphs">TARONA</text>
      <text class="title-city" x="73" y="127" font-size="62" textLength="255" lengthAdjust="spacingAndGlyphs">TARONA</text>
      <text class="title-main-shadow" x="68" y="378" font-size="255" textLength="690" lengthAdjust="spacingAndGlyphs">MIST FEST</text>
      <text class="title-main" x="80" y="368" font-size="255" textLength="690" lengthAdjust="spacingAndGlyphs">MIST FEST</text>
      <text class="title-year-shadow" x="555" y="470" font-size="118" textLength="218" lengthAdjust="spacingAndGlyphs">2018</text>
      <text class="title-year" x="551" y="466" font-size="118" textLength="218" lengthAdjust="spacingAndGlyphs">2018</text>
    </g>
  </svg>

  <p class="event-date">SATURDAY / 2ND JUNE / 12-10 PM</p>

  <section class="venue">
    <svg class="venue-shape" width="849" height="147" viewBox="0 0 849 147">
      <polygon points="65,0 785,0 700,147 155,147" fill="var(--black)"/>
    </svg>
    <h2 class="venue-name">The Corner Alehouse</h2>
    <p class="venue-address">52 MULGRAVE RD, KEREPUNI, HAMILTON</p>
  </section>

  <p class="features">VENDORS-PRIZES-COMPS-E JUICE AWARDS<br>ENTERTAINMENT-GIVEAWAYS &amp; MORE</p>

  <h3 class="tickets-heading">Get Your Tickets from</h3>
  <div class="age-badge age-badge--left">R18</div>
  <div class="age-badge age-badge--right">R18</div>
  <p class="tickets-url">www.taronamistfest.co.nz</p>
  <p class="tickets-store">THE CLOUD BARN</p>

  <section class="closing-banner">
    <svg class="closing-shape" width="849" height="76" viewBox="0 0 849 76">
      <polygon points="62,0 786,0 766,76 82,76" fill="var(--red)"/>
    </svg>
    <p class="closing-text">Come To Tarona's First Mist Fest</p>
  </section>

  <footer class="sponsors">
    <div class="sponsor sponsor--dark" style="width:98px">KORIMAKO VAPES</div>
    <div class="sponsor sponsor--dark" style="width:78px">POHUTU LIQUIDS</div>
    <div class="sponsor sponsor--light" style="width:52px">TAWHITI DRIP</div>
    <div class="sponsor sponsor--dark" style="width:98px">RANGI JUICES</div>
    <div class="sponsor sponsor--light" style="width:52px">MOANA CLOUDS</div>
    <div class="sponsor sponsor--light" style="width:96px">HARAKEKE DRIP</div>
    <div class="sponsor sponsor--light" style="width:52px">KUMARA BAR</div>
    <div class="sponsor sponsor--light" style="width:62px">PONGA LOFT</div>
  </footer>

</main>
</body>
</html>
```